Corvale Homes

To produce a business card design for our newly established house building and development company, We have had a logo design done please see attached, our slogan is "Crafting the place you call home"
Contact Information for Business Card
Adress on card needs to Read - 58 Elmsworth Lane, Thornbury Vale, Ashfordshire AV16 4QT. Director name Dean Vascotti
Requirements
Must have
- Web adress is www.corvale-homes.co.uk
- Email address is info@corvale-homes.co.uk
- phone number 07700 900417

```html
<!DOCTYPE html>
<html lang="en">
<head>
<meta charset="utf-8">
<title>Corvale Homes – Business Card</title>
<link rel="stylesheet" href="https://fonts.googleapis.com/css2?family=Ubuntu:wght@400;500;700&display=swap">
<style>
  :root {
    --green: #8cc044;
    --grey: #8c8c8c;
    --grey-light: #a3a3a3;
    --paper: #ffffff;
    --backdrop: #e8e7e4;
    --text-white: #ffffff;
  }
  * { box-sizing: border-box; margin: 0; padding: 0; }
  html, body {
    width: 1200px; height: 801px; overflow: hidden;
    background: var(--backdrop);
    font-family: "Ubuntu", sans-serif;
  }
  .card {
    position: absolute; top: 246px;
    width: 540px; height: 309px;
    background: var(--paper);
    box-shadow: 0 6px 18px rgba(0,0,0,0.12);
    overflow: hidden;
  }
  .card--front { left: 50px; }
  .card--back { left: 610px; }
  .card__bands { position: absolute; inset: 0; width: 100%; height: 100%; }

  /* front */
  .brand {
    position: absolute; left: 0; right: 0; top: 112px;
    text-align: center;
  }
  .brand__name {
    font-weight: 700; font-size: 44px; letter-spacing: 1px;
    color: var(--green); text-transform: uppercase; line-height: 1;
  }
  .brand__slogan {
    margin-top: 12px;
    font-weight: 400; font-size: 9px; letter-spacing: 5px;
    color: var(--green); text-transform: uppercase;
  }

  /* back */
  .brand--small { left: 26px; right: auto; top: 44px; text-align: left; }
  .brand--small .brand__name { font-size: 22px; letter-spacing: 0.5px; }
  .brand--small .brand__slogan { margin-top: 6px; font-size: 5px; letter-spacing: 2.5px; }

  .holder {
    position: absolute; right: 0; top: 112px;
    width: 186px; height: 64px;
    background: var(--grey);
    border-radius: 18px 0 0 18px;
    padding: 11px 0 0 22px;
    color: var(--text-white);
  }
  .holder__name { font-weight: 500; font-size: 19px; line-height: 1.1; }
  .holder__role { font-weight: 500; font-size: 15px; letter-spacing: 3px; margin-top: 4px; }

  .contacts {
    position: absolute; left: 24px; top: 170px;
    list-style: none;
  }
  .contact {
    display: flex; align-items: center; gap: 8px;
    height: 22px; margin-bottom: 4px;
  }
  .contact__icon { width: 17px; height: 17px; flex: none; }
  .contact__text {
    background: var(--grey-light);
    color: var(--text-white);
    font-size: 11.5px; line-height: 18px;
    padding: 0 7px; border-radius: 5px;
    white-space: nowrap;
  }
</style>
</head>
<body>

<section class="card card--front" aria-label="Business card front">
  <svg class="card__bands" viewBox="0 0 540 309" aria-hidden="true">
    <polygon points="0,0 236,0 226,16 0,16" fill="var(--green)"/>
    <polygon points="240,0 540,0 540,8 235,8" fill="var(--grey)"/>
    <polygon points="0,299 290,299 284,309 0,309" fill="var(--grey)"/>
    <polygon points="310,284 540,284 540,309 296,309" fill="var(--green)"/>
  </svg>
  <div class="brand">
    <p class="brand__name">Corvale Homes</p>
    <p class="brand__slogan">Crafting the place you call home</p>
  </div>
</section>

<section class="card card--back" aria-label="Business card back">
  <svg class="card__bands" viewBox="0 0 540 309" aria-hidden="true">
    <polygon points="0,0 320,0 312,10 0,10" fill="var(--grey)"/>
    <polygon points="330,0 540,0 540,26 312,26" fill="var(--green)"/>
    <line x1="0" y1="122" x2="360" y2="122" stroke="var(--green)" stroke-width="1.5"/>
    <polygon points="0,297 268,297 262,309 0,309" fill="var(--grey)"/>
    <polygon points="292,280 540,280 540,309 276,309" fill="var(--green)"/>
  </svg>

  <div class="brand brand--small">
    <p class="brand__name">Corvale Homes</p>
    <p class="brand__slogan">Crafting the place you call home</p>
  </div>

  <div class="holder">
    <p class="holder__name">Dean Vascotti</p>
    <p class="holder__role">Director</p>
  </div>

  <ul class="contacts">
    <li class="contact">
      <svg class="contact__icon" viewBox="0 0 20 20" aria-hidden="true">
        <circle cx="10" cy="10" r="10" fill="var(--green)"/>
        <circle cx="10" cy="10" r="5.5" fill="none" stroke="#fff" stroke-width="1.3"/>
        <ellipse cx="10" cy="10" rx="2.4" ry="5.5" fill="none" stroke="#fff" stroke-width="1.1"/>
        <line x1="4.5" y1="10" x2="15.5" y2="10" stroke="#fff" stroke-width="1.1"/>
      </svg>
      <span class="contact__text">www.corvale-homes.co.uk</span>
    </li>
    <li class="contact">
      <svg class="contact__icon" viewBox="0 0 20 20" aria-hidden="true">
        <circle cx="10" cy="10" r="10" fill="var(--green)"/>
        <rect x="5" y="6.5" width="10" height="7" fill="none" stroke="#fff" stroke-width="1.3"/>
        <polyline points="5,6.5 10,10.5 15,6.5" fill="none" stroke="#fff" stroke-width="1.2"/>
      </svg>
      <span class="contact__text">info@corvale-homes.co.uk</span>
    </li>
    <li class="contact">
      <svg class="contact__icon" viewBox="0 0 20 20" aria-hidden="true">
        <circle cx="10" cy="10" r="10" fill="var(--green)"/>
        <path d="M6.5 5.5l2 0 1 3-1.3 1a6 6 0 0 0 2.8 2.8l1-1.3 3 1 0 2c0 .6-.5 1-1 1A8.5 8.5 0 0 1 5.5 6.5c0-.5.4-1 1-1z" fill="#fff"/>
      </svg>
      <span class="contact__text">07700 900417</span>
    </li>
    <li class="contact">
      <svg class="contact__icon" viewBox="0 0 20 20" aria-hidden="true">
        <circle cx="10" cy="10" r="10" fill="var(--green)"/>
        <path d="M10 4.5a3.8 3.8 0 0 0-3.8 3.8c0 2.8 3.8 7.2 3.8 7.2s3.8-4.4 3.8-7.2A3.8 3.8 0 0 0 10 4.5z" fill="#fff"/>
        <circle cx="10" cy="8.3" r="1.4" fill="var(--green)"/>
      </svg>
      <span class="contact__text">58 Elmsworth Lane, Thornbury Vale, Ashfordshire AV16 4QT</span>
    </li>
  </ul>
</section>

</body>
</html>
```